Premium stylish simple clever card design for high end construction company.

I need a business card designed that is a standard size and shape (square edges) that is black in colour, with black edges. All text is to be either grey/silver or yellow/gold. On the front I want the logo (supplied as attachment g5) to be embossed or raised to give a texture. I also want the name of my company "The Kestrel Vault (larger font) construction co. (smaller font)" I like the clean style (found in attachment 56419286) of the black background with silver text. But the triangle is to be gold/yellow.

On the back needs to have my contact details. In silver or gold text.

Liam Porter - Builder
Liam@thekestrelvault.com.au
www.thekestrelvault.com.au
0427391065
Lic 517904k
PO BOX 739 Wrenhaven NSW 2188

Must look simple, elegant and precise.

My work is of the utmost quality and my business card needs to project that. It needs to be simple and precise. It should scream luxury and confidence. Feel free to get creative with the font and font size. If you google "The Kestrel Vault" you will see it has links to great architecture, art, nature and the fibonacci sequence so i am open to using these ideas also.

Target Market(s)

High End home owners. 30-70 year olds.

Industry/Entity Type

Residential Construction

Contact Information for Business Card

Logo and company name on front. Contact details on back.

Font styles to use
Serif
Sans Serif

Colors
ffcf3e

Requirements
Must have
• black background
Nice to have
• debossed logo (silver and gold)
• debased company name (silver)
Should not have
• It should not look like a standard construction business card with pictures of hammers or tools etc.

```html
<!DOCTYPE html>
<html lang="en">
<head>
<meta charset="utf-8">
<title>Liam Porter – The Kestrel Vault</title>
<link href="https://fonts.googleapis.com/css2?family=Carlito:wght@400;700&display=swap" rel="stylesheet">
<style>
  :root {
    --card-black: #000000;
    --gold: #c9b27a;
    --silver: #9e9e9e;
    --silver-dark: #6f6f6f;
    --rule: #8a8a8a;
  }
  html, body {
    margin: 0;
    padding: 0;
    width: 1200px;
    height: 667px;
    overflow: hidden;
    background: var(--card-black);
  }
  .card {
    position: relative;
    width: 1200px;
    height: 667px;
    background: var(--card-black);
    font-family: "Carlito", "Calibri", sans-serif;
    overflow: hidden;
  }
  .identity {
    position: absolute;
    right: 64px;
    top: 78px;
    text-align: right;
  }
  .identity__name {
    margin: 0;
    font-size: 48px;
    font-weight: 400;
    line-height: 56px;
    color: var(--gold);
  }
  .identity__role {
    margin: 0;
    font-size: 29px;
    line-height: 34px;
    color: var(--silver);
  }
  .brand__dot {
    position: absolute;
    left: 47px;
    top: 294px;
    width: 48px;
    height: 48px;
    border-radius: 50%;
    background: var(--silver-dark);
  }
  .brand__text {
    position: absolute;
    left: 105px;
    top: 300px;
    width: 192px;
    text-align: right;
    color: var(--silver);
    text-transform: uppercase;
    white-space: nowrap;
  }
  .brand__name {
    display: block;
    font-size: 19px;
    line-height: 22px;
    letter-spacing: 0.2px;
  }
  .brand__descriptor {
    display: block;
    font-size: 10px;
    line-height: 14px;
    letter-spacing: 0.3px;
    margin-top: 4px;
    padding-right: 2px;
  }
  .brand-rule {
    position: absolute;
    left: 0;
    top: 372px;
    width: 295px;
    height: 1px;
    background: var(--rule);
  }
  .contact {
    position: absolute;
    right: 64px;
    top: 406px;
    margin: 0;
    padding: 0;
    list-style: none;
    text-align: right;
    font-size: 32px;
    line-height: 40.5px;
    color: var(--silver);
  }
</style>
</head>
<body>
  <main class="card">
    <header class="identity">
      <h1 class="identity__name">Liam Porter</h1>
      <p class="identity__role">Builder</p>
    </header>

    <span class="brand__dot" aria-hidden="true"></span>
    <div class="brand__text">
      <span class="brand__name">The Kestrel Vault</span>
      <span class="brand__descriptor">Construction Co.</span>
    </div>
    <div class="brand-rule" aria-hidden="true"></div>

    <ul class="contact">
      <li class="contact__email">Liam@thekestrelvault.com.au</li>
      <li class="contact__web">www.thekestrelvault.com.au</li>
      <li class="contact__phone">0427391065</li>
      <li class="contact__licence">Lic 517904k</li>
      <li class="contact__address">PO BOX 739 Wrenhaven NSW 2188</li>
    </ul>
  </main>
</body>
</html>
```